They say laughter is the best medicine

This poster is for a nursing pharmacology class room with 70+students. Size is 24" x36". It needs to be a clean design. Would like vintage advertisement banners and script fonts. Would like a black background with an accent color. Please view pictures on word doc for examples.

```html
<!DOCTYPE html>
<html lang="en">
<head>
<meta charset="utf-8">
<title>Laughter Is the Best Medicine – Nursing Pharmacology Poster</title>
<link rel="stylesheet" href="https://fonts.googleapis.com/css2?family=Bowlby+One&family=Dancing+Script:wght@500;600&family=Quicksand:wght@600;700&family=Varela+Round&display=swap">
<style>
  :root {
    --canvas: #e9e9e8;
    --paper-top: #f1f1f3;
    --paper-mid: #e6e9ef;
    --paper-low: #f3dcda;
    --accent-red: #a82125;
    --script-red: #a8262a;
    --drug-blue: #2b63a8;
    --ink: #111111;
    --white: #ffffff;
  }
  * { box-sizing: border-box; margin: 0; padding: 0; }
  html, body {
    width: 1200px; height: 1200px; overflow: hidden;
    background: var(--canvas);
  }
  .poster {
    position: absolute; left: 220px; top: 40px;
    width: 760px; height: 1120px; overflow: hidden;
    background:
      radial-gradient(ellipse 260px 420px at 700px 240px, rgba(226,120,90,0.28), transparent 70%),
      linear-gradient(180deg, var(--paper-top) 0%, var(--paper-mid) 45%, var(--paper-low) 80%, #f4e6e4 100%);
    box-shadow: 0 6px 14px rgba(0,0,0,0.12);
  }
  .headline-laughter {
    position: absolute; left: 102px; top: 40px;
    font-family: "Bowlby One", "Arial Black", sans-serif;
    font-weight: 400; font-size: 93px; line-height: 1; letter-spacing: 0;
    color: var(--accent-red);
  }
  .headline-best {
    position: absolute; left: 184px; top: 118px;
    font-family: "Varela Round", "Quicksand", sans-serif;
    color: var(--ink); line-height: 1; white-space: nowrap;
  }
  .headline-best .small { font-size: 66px; }
  .headline-best .large { font-size: 97px; }
  .headline-medicine {
    position: absolute; left: 52px; top: 184px;
    font-family: "Dancing Script", cursive;
    font-weight: 500; font-size: 134px; line-height: 1;
    color: var(--script-red); white-space: nowrap;
  }
  .drug-block {
    position: absolute; left: 48px; top: 326px;
    font-family: "Quicksand", "Varela Round", sans-serif;
    font-weight: 700; color: var(--drug-blue);
  }
  .drug-block .lead { font-size: 69px; line-height: 1; margin-bottom: 6px; }
  .drug-list { list-style: none; }
  .drug-list li { font-size: 29px; line-height: 45.5px; white-space: nowrap; }
  .drug-list .sep { font-weight: 400; margin: 0 8px; }
  .drug-block .closing { font-size: 62px; line-height: 1; margin-top: 4px; }
  .drug-block .closing .amp { font-size: 32px; margin-right: 6px; }
  .tagline {
    position: absolute; left: 40px; top: 724px; width: 316px;
    text-align: center;
    font-family: "Dancing Script", cursive;
    font-weight: 500; font-size: 44px; line-height: 52px;
    color: var(--script-red); white-space: nowrap;
  }
  .nurse-photo {
    position: absolute; left: 331px; top: 280px;
    width: 429px; height: 697px;
  }
  .footer-band {
    position: absolute; left: 0; top: 977px;
    width: 760px; height: 143px;
    background: var(--accent-red);
    color: var(--white); text-align: center;
  }
  .course-title {
    margin-top: 20px;
    font-family: "Bowlby One", "Arial Black", sans-serif;
    font-weight: 400; font-size: 30px; line-height: 1; white-space: nowrap;
  }
  .course-title .cap { font-size: 37px; }
  .instructor {
    margin-top: 8px;
    font-family: "Quicksand", sans-serif; font-weight: 600;
    font-size: 23px; line-height: 1.2;
  }
  .role-line {
    display: flex; align-items: center; justify-content: center;
    gap: 18px; margin-top: 6px;
    font-family: "Quicksand", sans-serif; font-weight: 600;
    font-size: 23px;
  }
  .role-line .rule { width: 188px; height: 2px; background: var(--white); }
</style>
</head>
<body>
  <main class="poster">
    <h1 class="headline-laughter">LAUGHTER</h1>
    <div class="headline-best"><span class="small">is the </span><span class="large">best</span></div>
    <div class="headline-medicine">Medicine!</div>

    <svg class="nurse-photo" viewBox="0 0 429 697" role="img" aria-label="Photo of a smiling nurse in blue scrubs with a stethoscope around her neck">
      <defs>
        <linearGradient id="photoTone" x1="0" y1="0" x2="0" y2="1">
          <stop offset="0" stop-color="#e8e4e6" stop-opacity="0"/>
          <stop offset="0.3" stop-color="#d9dde6"/>
          <stop offset="0.55" stop-color="#3a6fb8"/>
          <stop offset="1" stop-color="#2f61aa"/>
        </linearGradient>
      </defs>
      <path d="M130 0 H429 V697 H0 L60 480 L125 380 Z" fill="url(#photoTone)"/>
    </svg>

    <section class="drug-block">
      <div class="lead">Sometimes</div>
      <ul class="drug-list">
        <li>Acetaminophen<span class="sep">|</span>Lorazepam</li>
        <li>Morphine<span class="sep">|</span>Furosemide</li>
        <li>Nitroglycerin<span class="sep">|</span>Haloperidol</li>
        <li>Loperamide<span class="sep">|</span>Albuterol</li>
        <li>Vancomycin<span class="sep">|</span>Insulin</li>
      </ul>
      <div class="closing"><span class="amp">&amp;</span>Oxygen</div>
    </section>

    <p class="tagline">are what you<br>need more than<br>laughter in<br>certain<br>situations.</p>

    <footer class="footer-band">
      <div class="course-title"><span class="cap">N</span>URSING <span class="cap">P</span>HARMACOLOGY <span class="cap">C</span>ONCEPTS</div>
      <div class="instructor">Laurel Whitcombe, PhD, MSN, RN, CCRN, CPN, CNE</div>
      <div class="role-line"><span class="rule"></span>Clinical Professor<span class="rule"></span></div>
    </footer>
  </main>
</body>
</html>
```